Bold Website Design for Fitness Trainer - No Coding

We are in need of a bold and unique website design for a personal fitness training company, www.TessaLorvel.com. We need DESIGN ONLY for three pages. These will be a homepage, a lead capture page, and one internal page with a sidebar. The design will be used for coding a wordpress theme, if that matters for the designer.

Tessa Lorvel Fitness Training
48 Larkfield Row, Suite 3
Brookvale, TX 00000
555-0148
http://www.tessalorvel.com

Target Market(s)

18-45 year old male and females making 80k+ a year and looking to get stronger and in shape.

Industry/Entity Type

Fitness

Number of Pages Required

3 page

Font styles to use
Sans Serif

Requirements
Must have
• See attached design specs file.
Nice to have
Should not have
• Boxed layout.
• Dark Background.

```html
<!DOCTYPE html>
<html lang="en">
<head>
<meta charset="utf-8">
<title>Tessa Lorvel Fitness Training</title>
<link href="https://fonts.googleapis.com/css2?family=Open+Sans:wght@400;600;700;800&display=swap" rel="stylesheet">
<style>
:root{
  --pink:#e3177b;
  --blue:#1aa6e0;
  --navy:#162536;
  --ink:#333d47;
  --muted:#7a848e;
  --light:#f1f3f5;
  --line:#dde2e7;
  --white:#ffffff;
  --dark:#15181c;
}
*{box-sizing:border-box;margin:0;padding:0}
html,body{width:1200px;height:3852px;overflow:hidden}
body{font-family:'Open Sans',Arial,sans-serif;color:var(--ink);background:var(--white);font-size:14px;line-height:1.6}
.wrap{width:960px;margin:0 auto;position:relative}
.topbar{height:32px;background:var(--navy);color:#cfd8e2;font-size:12px}
.topbar .wrap{display:flex;align-items:center;height:32px;gap:28px}
.topbar .item{display:flex;align-items:center;gap:6px}
.topbar .socials{margin-left:auto;display:flex;gap:6px}
.sq{width:18px;height:18px;background:#3b4d61;display:inline-block}
.header{height:144px;background:var(--white)}
.header .wrap{height:144px;display:flex;align-items:center;justify-content:center;gap:16px}
.logo-mark{width:92px;height:92px;border-radius:50%;background:var(--pink)}
.logo-name{font-size:44px;font-weight:800;color:var(--navy);letter-spacing:.5px}
.nav{height:40px;background:var(--pink)}
.nav ul{list-style:none;display:flex;height:40px}
.nav li{padding:0 26px;line-height:40px;color:var(--white);font-weight:700;font-size:13px;text-transform:uppercase}
.nav li.active{background:var(--blue)}
.hero{height:484px;background:linear-gradient(120deg,#9fb7cf,#e8e2dc 45%,#6f8fb3)}
.band{background:var(--blue);color:var(--white);text-align:center}
.getstarted{height:280px;padding-top:48px}
.band h2{font-size:20px;font-weight:700;text-transform:uppercase;letter-spacing:1px}
.band .rule{width:50px;height:2px;background:var(--white);margin:10px auto 18px}
.band p{font-size:15px;line-height:1.7}
.btn-outline{display:inline-block;margin-top:26px;border:2px solid var(--white);padding:8px 22px;font-weight:700;font-size:13px;text-transform:uppercase}
.section-title{color:var(--blue);font-size:20px;font-weight:800;text-transform:uppercase;text-align:center}
.section-title+.rule{width:50px;height:2px;background:var(--pink);margin:8px auto 14px}
.services{height:408px;padding-top:40px}
.services .lead{text-align:center;color:var(--muted);font-size:13px;width:720px;margin:0 auto 24px}
.cards{display:flex;gap:20px}
.card{flex:1}
.card .photo{height:150px}
.card .label{height:34px;line-height:34px;text-align:center;font-weight:600;font-size:14px;background:var(--light);color:var(--ink)}
.card.active .label{background:var(--pink);color:var(--white)}
.testimonials{height:352px;background:var(--dark);color:#d7dce1;text-align:center;padding-top:30px;position:relative}
.avatar{width:88px;height:88px;border-radius:50%;background:linear-gradient(#c99b7f,#8a5e49);margin:18px auto 20px;border:3px solid var(--white)}
.testimonials blockquote{width:820px;margin:0 auto;font-size:14px;color:#c7ccd2}
.testimonials cite{display:block;margin-top:14px;color:var(--pink);font-style:normal;font-weight:700}
.arrow{position:absolute;top:182px;width:30px;height:30px;border-radius:50%;background:#2c3138}
.arrow svg{display:block;margin:8px auto}
.arrow.l{left:160px}.arrow.r{right:160px}
.social{height:640px;padding-top:40px}
.panels{display:flex;gap:60px}
.panel{flex:1;border:1px solid var(--line);height:520px}
.panel .bar{height:38px;background:var(--navy);color:var(--white);font-weight:700;font-size:13px;display:flex;align-items:center;gap:10px;padding:0 14px}
.panel .bar .sq{background:var(--white);width:14px;height:14px}
.fb-body{padding:14px;font-size:12px;color:var(--ink)}
.fb-head{display:flex;gap:10px;align-items:center;margin-bottom:12px}
.fb-head .pic{width:44px;height:44px;background:#8aa3bb}
.fb-like{display:inline-block;background:#4a6ea8;color:var(--white);font-size:11px;padding:1px 8px;margin-top:4px}
.fb-post{border:1px solid var(--line);padding:10px}
.fb-post p{margin-bottom:10px}
.fb-post .img{height:140px;width:180px;background:linear-gradient(#6b7d8e,#c3b9ad)}
.fb-strip{display:flex;gap:6px;margin-top:14px}
.fb-strip span{flex:1;height:46px;background:#a9b6c3}
.ig-stats{display:flex;justify-content:space-around;padding:10px 0;font-size:12px;text-align:center;border-bottom:1px solid var(--line)}
.ig-stats b{display:block;font-size:15px}
.ig-photo{height:330px;margin:14px;background:linear-gradient(#d6cfc6,#7f6f62)}
.ig-meta{padding:0 14px;font-size:12px;color:var(--muted)}
.blog{height:840px;background:var(--light);padding-top:40px}
.post{display:flex;gap:20px;background:var(--white);margin-bottom:14px;height:232px}
.post .thumb{width:300px;flex:none}
.post .text{padding:14px 16px 0 0}
.post h3{color:var(--blue);font-size:15px;font-weight:700}
.post .date{font-size:12px;color:var(--muted);margin:4px 0 8px;display:flex;align-items:center;gap:6px}
.post p{font-size:12.5px;color:#5b6570;line-height:1.65}
.post .more{display:block;margin-top:8px;font-weight:700;font-size:12px;color:var(--ink)}
.cta{height:280px;padding-top:52px}
.footer{height:300px;padding-top:36px;background:var(--white)}
.cols{display:flex;gap:40px}
.col h4{color:var(--blue);font-size:14px;font-weight:800;text-transform:uppercase;margin-bottom:14px}
.col.touch{width:260px;font-size:13px}
.col.touch p{margin-bottom:6px}
.col.touch .socials{display:flex;gap:8px;margin-top:14px}
.col.touch .sq{background:var(--navy);width:24px;height:24px}
.col.form{width:400px;padding-top:30px}
.form-row{display:flex;gap:10px;margin-bottom:10px}
.field{flex:1;height:34px;border:1px solid var(--line);font-size:12px;color:var(--muted);padding:7px 10px}
.field.area{height:74px}
.send{background:var(--blue);color:var(--white);text-align:center;height:36px;line-height:36px;font-weight:700;font-size:13px;text-transform:uppercase}
.col.links{margin-left:auto;width:180px}
.col.links ul{list-style:none;font-size:13px}
.col.links li{border-bottom:1px solid var(--line);padding:4px 0;display:flex;align-items:center;gap:8px}
.col.links li::before{content:"";width:6px;height:6px;background:var(--pink)}
.bottombar{height:52px;background:var(--navy);color:#aeb9c6;font-size:12px}
.bottombar .wrap{display:flex;justify-content:space-between;align-items:center;height:52px}
.bottombar .phone{color:var(--blue);font-weight:700}
</style>
</head>
<body>
<div class="topbar"><div class="wrap">
  <span class="item"><svg width="12" height="12" viewBox="0 0 24 24"><path fill="#cfd8e2" d="M6.6 10.8a15 15 0 006.6 6.6l2.2-2.2a1 1 0 011-.25 11.4 11.4 0 003.6.6 1 1 0 011 1V20a1 1 0 01-1 1A17 17 0 013 4a1 1 0 011-1h3.5a1 1 0 011 1c0 1.25.2 2.45.6 3.6a1 1 0 01-.25 1z"/></svg>555-0148</span>
  <span class="item"><svg width="12" height="12" viewBox="0 0 24 24"><rect x="3" y="5" width="18" height="14" fill="none" stroke="#cfd8e2" stroke-width="2"/><path d="M3 6l9 7 9-7" fill="none" stroke="#cfd8e2" stroke-width="2"/></svg>Training Consultant</span>
  <span class="item"><svg width="12" height="12" viewBox="0 0 24 24"><circle cx="12" cy="12" r="9" fill="none" stroke="#cfd8e2" stroke-width="2"/><path d="M12 7v5l3 3" fill="none" stroke="#cfd8e2" stroke-width="2"/></svg>Training Schedule</span>
  <span class="socials"><i class="sq"></i><i class="sq"></i><i class="sq"></i><i class="sq"></i><i class="sq"></i></span>
</div></div>

<header class="header"><div class="wrap">
  <span class="logo-mark"></span><span class="logo-name">Tessa Lorvel</span>
</div></header>

<nav class="nav"><div class="wrap"><ul>
  <li class="active">Home</li><li>Programs</li><li>Meet Your Trainer</li><li>Blog</li><li>Contact Me</li><li>Free Sessions</li>
</ul></div></nav>

<div class="hero" role="img" aria-label="Photo of a group fitness class stretching in a bright gym"></div>

<section class="band getstarted">
  <h2>Get Started</h2><div class="rule"></div>
  <p>Get Started Today - Your First Sessions is Free!<br>General Fitness - Weight Loss - Strength Training - Powerlifting</p>
  <span class="btn-outline">Get Started &#8250;</span>
</section>

<section class="services"><div class="wrap">
  <h2 class="section-title">Our Services</h2><div class="rule"></div>
  <p class="lead">Lorem ipsum dolor sit amet consectetur adipiscing elit sed do eiusmod tempor incididunt ut labore et dolore magna aliqua enim minim.</p>
  <div class="cards">
    <div class="card active"><div class="photo" role="img" aria-label="Photo of a fitness consultation" style="background:linear-gradient(#c9a48f,#6e7f93)"></div><div class="label">Fitness Consultation</div></div>
    <div class="card"><div class="photo" role="img" aria-label="Photo of a personal training session" style="background:linear-gradient(#b9c6d3,#d77aa6)"></div><div class="label">Personal Training</div></div>
    <div class="card"><div class="photo" role="img" aria-label="Photo of strength training equipment" style="background:linear-gradient(#8fa3b6,#3e4f62)"></div><div class="label">Strength and Conditioning</div></div>
  </div>
</div></section>

<section class="testimonials">
  <h2 class="section-title">What Do Our Clients Say</h2>
  <div class="avatar" role="img" aria-label="Client portrait"></div>
  <blockquote>Lorem ipsum dolor sit amet, consectetur adipiscing elit, sed do eiusmod tempor incididunt ut labore et dolore magna aliqua. Sed fermentum dolor quis nisl tincidunt, nec tempus erat porta vitae lacus sed dignissim fringilla mauris sit amet auctor.<cite>Lorem Ipsum</cite></blockquote>
  <span class="arrow l"><svg width="14" height="14" viewBox="0 0 14 14"><path d="M9 2L4 7l5 5" fill="none" stroke="#fff" stroke-width="2"/></svg></span>
  <span class="arrow r"><svg width="14" height="14" viewBox="0 0 14 14"><path d="M5 2l5 5-5 5" fill="none" stroke="#fff" stroke-width="2"/></svg></span>
</section>

<section class="social"><div class="wrap">
  <h2 class="section-title">Get Connect Social</h2><div class="rule"></div>
  <div class="panels">
    <div class="panel">
      <div class="bar"><i class="sq"></i>Like Me on Circlebook</div>
      <div class="fb-body">
        <div class="fb-head"><span class="pic" role="img" aria-label="Page profile photo"></span><div><b>Tessa Lorvel</b><br><span class="fb-like">Like</span></div></div>
        <div class="fb-post">
          <p><b>Tessa Lorvel</b><br>Had a great session with the team this morning and we are still going strong. Another great training day done!</p>
          <div class="img" role="img" aria-label="Post photo from a gym session"></div>
        </div>
        <div class="fb-strip"><span></span><span></span><span></span><span></span><span></span><span></span></div>
      </div>
    </div>
    <div class="panel">
      <div class="bar"><i class="sq"></i>Follow Me on Snapgrid</div>
      <div class="ig-stats"><div><b>2995</b>posts</div><div><b>351</b>followers</div><div><b>2,650</b>following</div></div>
      <div class="ig-photo" role="img" aria-label="Photo of the trainer posing in workout wear"></div>
      <div class="ig-meta">&#9829; 0 &nbsp;&nbsp; &#9679; 0</div>
    </div>
  </div>
</div></section>

<section class="blog"><div class="wrap">
  <h2 class="section-title">Latest Blog Post</h2><div class="rule"></div>
  <article class="post">
    <div class="thumb" role="img" aria-label="Photo of a client training shoulders in the gym" style="background:linear-gradient(#6c8ab0,#d7c2b0)"></div>
    <div class="text"><h3>Chest, Shoulders, Triceps and Back</h3>
      <div class="date"><svg width="12" height="12" viewBox="0 0 24 24"><rect x="3" y="5" width="18" height="16" fill="none" stroke="#7a848e" stroke-width="2"/><path d="M3 10h18" stroke="#7a848e" stroke-width="2"/></svg>December 16 , 2014</div>
      <p>This is our training tip for upper body day. Start with a light warm up, move into presses for chest and shoulders, then finish with rows for the back. Keep the rest short, drink water between sets and focus on clean form through every single rep. Next week we add heavier sets.</p>
      <span class="more">Read more</span></div>
  </article>
  <article class="post">
    <div class="thumb" role="img" aria-label="Photo of motivational words printed on paper" style="background:linear-gradient(#e6e3dc,#9a958c)"></div>
    <div class="text"><h3>What Motivates Me To Be Healthy and Stay Fit</h3>
      <div class="date"><svg width="12" height="12" viewBox="0 0 24 24"><rect x="3" y="5" width="18" height="16" fill="none" stroke="#7a848e" stroke-width="2"/><path d="M3 10h18" stroke="#7a848e" stroke-width="2"/></svg>December 16 , 2014</div>
      <p>People often ask me what keeps me going each day. For me it is simple: feeling strong, sleeping well and being there for the people I train. Small daily habits add up, and a good plan makes the hard days easier. Here is how I stay on track all year long.</p>
      <span class="more">Read more</span></div>
  </article>
  <article class="post">
    <div class="thumb" role="img" aria-label="Photo of a client lifting weights" style="background:linear-gradient(#5a6f86,#b7c4d1)"></div>
    <div class="text"><h3>Chest, Shoulders, Triceps and Back</h3>
      <div class="date"><svg width="12" height="12" viewBox="0 0 24 24"><rect x="3" y="5" width="18" height="16" fill="none" stroke="#7a848e" stroke-width="2"/><path d="M3 10h18" stroke="#7a848e" stroke-width="2"/></svg>December 16 , 2014</div>
      <p>This is our training tip for upper body day. Start with a light warm up, move into presses for chest and shoulders, then finish with rows for the back. Keep the rest short, drink water between sets and focus on clean form through every single rep. Next week we add heavier sets.</p>
      <span class="more">Read more</span></div>
  </article>
</div></section>

<section class="band cta">
  <h2>Visitor To Get Started Today</h2><div class="rule"></div>
  <p>Get Started Today - Your First Sessions is Free!<br>General Fitness - Weight Loss - Strength Training - Powerlifting</p>
  <span class="btn-outline">Get Started Today &#8250;</span>
</section>

<footer class="footer"><div class="wrap"><div class="cols">
  <div class="col touch"><h4>Get In Touch</h4>
    <p>Tessa Lorvel Fitness Training<br>48 Larkfield Row, Suite 3<br>Brookvale, TX 00000</p>
    <p>555-0148</p>
    <p>hello@tessalorvel.com</p>
    <div class="socials"><i class="sq"></i><i class="sq"></i><i class="sq"></i><i class="sq"></i><i class="sq"></i></div>
  </div>
  <div class="col form">
    <div class="form-row"><span class="field">Your Name...</span><span class="field">Your email...</span></div>
    <div class="form-row"><span class="field area">Your Message...</span></div>
    <div class="send">Send Message</div>
  </div>
  <div class="col links"><h4>Resource Links</h4>
    <ul><li>Home</li><li>Programs</li><li>Meet Your Trainer</li><li>Blog</li><li>Contact Me</li><li>Free Session</li></ul>
  </div>
</div></div></footer>

<div class="bottombar"><div class="wrap">
  <span>Copyright &copy; 2014 Tessa Lorvel. All rights reserved.</span>
  <span class="phone">555-0148</span>
  <span>Privacy Policy | Terms &amp; Conditions</span>
</div></div>
</body>
</html>
```